Real eatate

My company name is “Silver Heron Realestate” i would like to create a business card. I would like something modern and sleek similar to picture uploaded. All text in the business card should be black and the logo gold any shade.

```html
<!DOCTYPE html>
<html lang="en">
<head>
<meta charset="utf-8">
<title>Silver Heron Realestate – Business Card</title>
<link rel="stylesheet" href="https://fonts.googleapis.com/css2?family=Poppins:wght@400;500;600&display=swap">
<style>
  :root {
    --page-bg: #e9e9e9;
    --card-white: #ffffff;
    --card-black: #0b0b0b;
    --card-black-glow: #2a2a2a;
    --ink: #111111;
    --gold: #c99a2e;
    --gold-light: #e4c25a;
  }
  * { margin: 0; padding: 0; box-sizing: border-box; }
  html, body {
    width: 1200px; height: 900px; overflow: hidden;
    background: var(--page-bg);
    font-family: "Poppins", sans-serif;
  }
  .canvas { position: relative; width: 1200px; height: 900px; }

  .card {
    position: absolute; left: 250px;
    width: 700px; height: 400px;
    border-radius: 22px;
    box-shadow: 0 10px 30px rgba(0,0,0,.18);
    overflow: hidden;
  }
  .card--back {
    top: 40px;
    background: radial-gradient(ellipse at 50% 45%, var(--card-black-glow) 0%, var(--card-black) 65%);
    display: flex; align-items: center; justify-content: center;
  }
  .card--front { top: 470px; background: var(--card-white); }

  .wordmark {
    display: flex; align-items: center; gap: 16px;
    color: var(--gold);
    font-weight: 500;
    text-transform: uppercase;
  }
  .wordmark__dot {
    width: 44px; height: 44px; border-radius: 50%;
    background: var(--gold);
    flex-shrink: 0;
  }
  .wordmark__text { font-size: 24px; line-height: 1.25; letter-spacing: 2px; }

  .card--front .wordmark {
    position: absolute; left: 40px; top: 0; bottom: 0;
    flex-direction: column; justify-content: center; gap: 18px;
    width: 270px; text-align: center;
  }
  .card--front .wordmark__dot { width: 70px; height: 70px; }
  .card--front .wordmark__text { font-size: 21px; }

  .divider {
    position: absolute; left: 340px; top: 60px;
    width: 1.5px; height: 280px; background: var(--gold);
  }

  .contact {
    position: absolute; left: 375px; top: 62px;
    color: var(--ink);
  }
  .contact__name { font-size: 32px; font-weight: 600; line-height: 1.1; }
  .contact__title { font-size: 17px; color: var(--gold); margin-bottom: 16px; }
  .contact__list { list-style: none; font-size: 17px; line-height: 1.55; }
  .contact__item { display: flex; align-items: flex-start; gap: 12px; }
  .contact__icon { width: 16px; height: 16px; margin-top: 5px; flex-shrink: 0; fill: var(--gold); }
  .contact__address { line-height: 1.4; margin-top: 4px; }
</style>
</head>
<body>
<main class="canvas">

  <section class="card card--back" aria-label="Card back">
    <div class="wordmark">
      <span class="wordmark__dot"></span>
      <span class="wordmark__text">Silver Heron<br>Realestate</span>
    </div>
  </section>

  <section class="card card--front" aria-label="Card front">
    <div class="wordmark">
      <span class="wordmark__dot"></span>
      <span class="wordmark__text">Silver Heron<br>Realestate</span>
    </div>

    <div class="divider"></div>

    <div class="contact">
      <div class="contact__name">Daniel Reyes</div>
      <div class="contact__title">Project Manager</div>
      <ul class="contact__list">
        <li class="contact__item">
          <svg class="contact__icon" viewBox="0 0 16 16"><path d="M3.6 1.5l2.3 2.6-1.3 1.9c.9 2 2.5 3.6 4.5 4.5l1.9-1.3 2.6 2.3-1.5 2.3C7.2 13.5 2.5 8.8 1.3 3z"/></svg>
          <span>555 014 2786</span>
        </li>
        <li class="contact__item">
          <svg class="contact__icon" viewBox="0 0 16 16"><path d="M4 1h8v4H4zM1 6h14v6h-3v3H4v-3H1zm4 4v4h6v-4z"/></svg>
          <span>555 014 2786</span>
        </li>
        <li class="contact__item">
          <svg class="contact__icon" viewBox="0 0 16 16"><path d="M1 3h14v10H1zm1.5 1.2V5l5.5 4 5.5-4v-.8L8 8z"/></svg>
          <span>hello@silverheron.com</span>
        </li>
        <li class="contact__item">
          <svg class="contact__icon" viewBox="0 0 16 16"><path d="M8 1a7 7 0 100 14A7 7 0 008 1zm0 1.4c.8 0 1.7 1.6 2 4.1H6c.3-2.5 1.2-4.1 2-4.1zM2.5 7.5h2.3c0 .4 0 .7 0 1H2.5a5.6 5.6 0 010-1zm.3 2.3h2.2c.2 1.2.5 2.2 1 3a5.6 5.6 0 01-3.2-3zm3.2 0h4c-.3 2.3-1.2 3.8-2 3.8s-1.7-1.5-2-3.8zm5 0h2.2a5.6 5.6 0 01-3.2 3c.5-.8.8-1.8 1-3zm.2-1.3c0-.3 0-.6 0-1h2.3a5.6 5.6 0 010 1zM11 6.5c-.2-1.3-.5-2.3-1-3.1a5.6 5.6 0 013.2 3.1zm-6 0H2.8A5.6 5.6 0 016 3.4c-.5.8-.8 1.8-1 3.1z"/></svg>
          <span>www.silverheron.com</span>
        </li>
        <li class="contact__item">
          <svg class="contact__icon" viewBox="0 0 16 16"><path d="M8 1a5 5 0 00-5 5c0 3.8 5 9 5 9s5-5.2 5-9a5 5 0 00-5-5zm0 7a2 2 0 110-4 2 2 0 010 4z"/></svg>
          <span class="contact__address">118 Harbor Lane<br>Suite 210, Lakeview<br>OR 97000</span>
        </li>
      </ul>
    </div>
  </section>

</main>
</body>
</html>
```